Vorbel Neutraceuticals Needs a New Label Design!

Vorbel is a neutraceutical line of vitamins, supplements and protein powders. We are looking for a new look/feel for our labels to really make them pop off the shelf.

Some brands we like are:
www.pemsy.com
www.kelvorida.com
www.dubrin.com

We are going to have square bottles and caps that will most likely be white or clear. We'd like a look/feel that uses bold colors and perhaps foil to make the design stand out.

The labels may be different colors for each product, but the general look/feel should be the same. To learn more about Vorbel, take a look at www.qtremedics.com/vorbel.

We are also reformulating to make our products natural, organic and non-GMO. A look gearing more towards a holistic feel might work!

We have a logo that we cannot change, but we are not committed to the colors of it (Orange and green) and it does NOT have to be prominent on the label itself.

Design must utilize our icons (see website and attached files)

Vorbels tagline is: Shaping Strong Lives
Updates

Project Deadline Extended
Reason: We wanted to extend this project to give designers a bit more time to work on it!

Target Market(s)

Women and Men who are serious about their health, women purchasing vitamins for family....

Industry/Entity Type

Health And Wellness

Font styles to use
Decorative

Requirements
Must have
• Must:
• -Utilize our icons
• -Have bold colors
• -Stand out on a shelf
Nice to have
• The "Bel" in "Vorbel" should stand out

```html
<!DOCTYPE html>
<html lang="en">
<head>
<meta charset="utf-8">
<title>Vorbel Vitamin D Label</title>
<link rel="stylesheet" href="https://fonts.googleapis.com/css2?family=Archivo+Black&family=Arimo:ital,wght@0,400;0,700;1,400&family=Josefin+Sans:wght@300;400&display=swap">
<style>
:root{
  --page:#efe9e2;
  --red:#d8242f;
  --red-deep:#c0152a;
  --orange:#f07a1e;
  --yellow:#fbc53a;
  --cream:#fbe9ee;
  --ink:#1c1c1c;
  --white:#ffffff;
  --icon-red:#e02a2e;
  --icon-yellow:#f6bf1c;
  --icon-blue:#2f9ed8;
  --icon-purple:#6a3a94;
  --icon-teal:#2bb39c;
}
*{box-sizing:border-box;margin:0;padding:0}
html,body{width:1200px;height:1200px;overflow:hidden;background:var(--page)}
body{position:relative;font-family:"Arimo",Arial,sans-serif}
.label{position:absolute;left:40px;top:409px;width:1120px;height:382px;overflow:hidden;box-shadow:0 6px 18px rgba(0,0,0,.18)}
.label-art{position:absolute;inset:0;
  background:
    radial-gradient(ellipse 26% 48% at 50% 42%, rgba(252,230,240,1) 0%, rgba(252,230,240,.85) 35%, rgba(252,230,240,0) 75%),
    radial-gradient(ellipse 38% 60% at 30% 70%, rgba(255,236,120,.55) 0%, rgba(255,236,120,0) 70%),
    radial-gradient(ellipse 38% 60% at 70% 70%, rgba(255,236,120,.55) 0%, rgba(255,236,120,0) 70%),
    linear-gradient(90deg, var(--red) 0%, #ea4a2a 12%, var(--orange) 28%, var(--yellow) 42%, var(--yellow) 58%, var(--orange) 72%, #ea4a2a 88%, var(--red) 100%);}
.label-art::after{content:"";position:absolute;left:0;right:0;bottom:0;height:8px;background:var(--red-deep)}

.directions{position:absolute;left:64px;top:49px;width:272px;height:294px;border:1px solid rgba(255,255,255,.8);border-radius:6px;background:rgba(214,40,40,.55);color:var(--white);padding:10px 10px;font-size:9px;line-height:11.4px}
.directions p{margin-bottom:11px;text-align:justify}
.directions p b{font-weight:700}
.directions .warning{font-weight:700;font-size:10px;line-height:12.4px;text-align:left;margin-left:-3px;margin-bottom:10px}
.directions .disclaimer{text-align:left;font-size:9.4px}

.brand{position:absolute;left:450px;top:24px;width:270px;text-align:center}
.brand-name{position:absolute;left:471px;top:118px;font-family:"Josefin Sans",sans-serif;font-weight:300;font-size:66px;line-height:1;color:var(--ink)}
.product{position:absolute;left:473px;top:194px;font-family:"Archivo Black",sans-serif;font-size:37px;line-height:1;color:#e8402a;letter-spacing:-1px}
.category{position:absolute;left:472px;top:243px;width:230px;height:25px;border-bottom:2px solid var(--red);background:linear-gradient(90deg,rgba(255,255,255,.85),rgba(255,255,255,.5));font-family:"Josefin Sans",sans-serif;font-size:21px;line-height:26px;padding-left:6px;color:var(--ink)}
.tagline{position:absolute;left:474px;top:272px;font-style:italic;font-size:12.2px;line-height:16px;color:#4a3a34}

.icons{position:absolute;left:473px;top:323px;display:flex;gap:4px}
.icon{width:30px;height:25px;display:flex;align-items:center;justify-content:center}
.icon svg{width:18px;height:18px;fill:none;stroke:var(--white);stroke-width:1.6;stroke-linecap:round;stroke-linejoin:round}
.i-heart{background:var(--icon-red)}.i-eye{background:var(--icon-yellow)}.i-brain{background:var(--icon-blue)}.i-pill{background:var(--icon-purple)}.i-joint{background:var(--icon-teal)}

.count{position:absolute;left:651px;top:307px;width:58px;height:58px;border-radius:50%;background:radial-gradient(circle at 40% 35%,#ee4234,#c81d24);color:var(--white);text-align:center;font-family:"Archivo Black",sans-serif;font-size:22px;line-height:1;padding-top:10px}
.count span{display:block;font-family:"Arimo",sans-serif;font-size:11px;background:#d8242f;border:1px solid rgba(255,255,255,.7);margin:2px -16px 0 -2px;padding:1px 0}

.supply{position:absolute;left:658px;top:0;width:44px;height:76px;background:linear-gradient(#f58a25,#e8572a);border-radius:0 0 3px 3px;color:var(--white);text-align:center;line-height:1}
.supply b{display:block;font-family:"Archivo Black",sans-serif;font-size:24px;margin-top:16px}
.supply span{display:block;font-size:15px;font-weight:400}
.supply small{display:block;font-size:9px}

.facts{position:absolute;left:844px;top:34px;width:214px;height:319px;background:var(--cream);border:2px solid var(--ink);padding:3px 4px;color:var(--ink);font-size:7.2px}
.facts h2{font-family:"Archivo Black",sans-serif;font-size:15px;line-height:16px;font-weight:400;letter-spacing:.3px}
.facts .serving{font-size:7.6px;line-height:9px;border-bottom:4px solid var(--ink);padding-bottom:3px}
.facts .head{display:flex;justify-content:space-between;font-weight:700;font-size:8px;padding:2px 0;border-bottom:2px solid var(--ink)}
.row{display:grid;grid-template-columns:1fr 38px 30px;border-bottom:1px solid var(--ink);line-height:10.4px}
.row b{font-weight:700}
.row .amt{text-align:right}.row .dv{text-align:right}
.row .sub{grid-column:1/4;line-height:7.2px;font-size:6.8px;margin-top:-1px;padding-bottom:1px}
.facts .foot{border-top:2px solid var(--ink);margin-top:1px;padding-top:2px;font-size:6.4px;font-weight:700}
</style>
</head>
<body>
<main class="label">
  <div class="label-art" role="img" aria-label="Warm abstract backdrop of red, orange and yellow light rays with soft floating bubbles"></div>

  <section class="directions">
    <p><b>SUGGESTED USE:</b> Two capsules taken daily with meals as a dietary supplement, or as directed by a health care professional.</p>
    <p><b>CAUTION:</b> Do not exceed recommended dose. This Product is not intended for pregnant or nursing mothers, children under the age of 18 or persons with a known medical condition including any pressure). If you have questions about the advisability of taking this product, consult your physician prior to use. This Product is manufactured and packaged in afacility which may also process milk, soy, wheat, egg, peanuts, tree nuts, fish and crustacean shellfish. This product is manufactured and packaged in a facility which may also process milk, soy, wheat, egg, peanuts, tree nuts, fish and crustacean shellfish.</p>
    <p class="warning">KEEP OUT OF REACH OF CHILDREN,<br>DO NOT USE IF SAFETY SEAL IS DAMAGED OR MISSING. STORE IN A COOL, DRY PLACE.</p>
    <p class="disclaimer">These statements have not been evaluated by the Food and Drug Administration. This Product is not intended to treat, cure, prevent or diagnose any disease.</p>
  </section>

  <div class="supply"><b>30</b><span>DAY</span><small>SUPPLY</small></div>

  <h1 class="brand-name">Vorbel</h1>
  <div class="product">VITAMIN-D</div>
  <div class="category">Dietary Supplement</div>
  <p class="tagline">Excellent source of natural Vitamin D<br>and blah blah blah blah blah</p>

  <div class="icons">
    <div class="icon i-heart"><svg viewBox="0 0 20 20"><path d="M10 17 3 10a4 4 0 0 1 7-5 4 4 0 0 1 7 5z"/><path d="M4 10h4l1-2 2 4 1-2h4"/></svg></div>
    <div class="icon i-eye"><svg viewBox="0 0 20 20"><path d="M2 10s3-5 8-5 8 5 8 5-3 5-8 5-8-5-8-5z"/><circle cx="10" cy="10" r="2.5"/></svg></div>
    <div class="icon i-brain"><svg viewBox="0 0 20 20"><circle cx="10" cy="10" r="7"/><path d="M10 3v14M5 7q3 2 0 6M15 7q-3 2 0 6"/></svg></div>
    <div class="icon i-pill"><svg viewBox="0 0 20 20"><rect x="2" y="7" width="16" height="6" rx="3" transform="rotate(30 10 10)"/><path d="M8 6.5 12 13.5"/></svg></div>
    <div class="icon i-joint"><svg viewBox="0 0 20 20"><path d="M7 2v6l3 3-2 7M13 2v6l-2 2M12 12l1 6"/></svg></div>
  </div>

  <div class="count">180<span>CAPSULES</span></div>

  <section class="facts">
    <h2>Supplement Facts</h2>
    <div class="serving">Serving Size : 2 Capsules</div>
    <div class="head"><span>Amount Per Serving</span><span>%Daily Value</span></div>
    <div class="row"><span><b>Vitamin C</b> (ascorbic acid)</span><span class="amt">30mg</span><span class="dv">50%</span></div>
    <div class="row"><span><b>Vitamin E</b> (d-Alpha toco.)</span><span class="amt">30mg</span><span class="dv">100%</span></div>
    <div class="row"><span><b>Selenium</b> (amino acid chelate)</span><span class="amt">20mcg</span><span class="dv">29%</span></div>
    <div class="row"><span><b>Graviola</b> (powder)</span><span class="amt">300mg</span><span class="dv">*</span></div>
    <div class="row"><span><b>Red Raspberry Juice Extract</b></span><span class="amt">200mg</span><span class="dv">*</span></div>
    <div class="row"><span><b>Green Tea</b> (40% extract)</span><span class="amt">200mg</span><span class="dv">*</span></div>
    <div class="row"><span><b>Curcumin</b> (powder)</span><span class="amt">100mg</span><span class="dv">*</span></div>
    <div class="row"><span><b>Beta-Glucan</b></span><span class="amt">100mg</span><span class="dv">*</span></div>
    <div class="row"><span><b>Cat's Claw</b> (powder)</span><span class="amt">20mg</span><span class="dv">*</span></div>
    <div class="row"><span><b>Garlic</b> (powder)</span><span class="amt">20mg</span><span class="dv">*</span></div>
    <div class="row"><span><b>Korean Ginseng</b> (powder)</span><span class="amt">20mg</span><span class="dv">*</span></div>
    <div class="row"><span><b>Lycopene</b></span><span class="amt">2mg</span><span class="dv">*</span></div>
    <div class="row"><span><b>Quercetin</b></span><span class="amt">50mg</span><span class="dv">*</span></div>
    <div class="row"><span><b>Pine Bark</b> (95% extract)</span><span class="amt">100mg</span><span class="dv">*</span></div>
    <div class="row"><span><b>Grape Seed</b> (95% extract)</span><span class="amt">100mg</span><span class="dv">*</span></div>
    <div class="row"><span><b>Pomegranate</b> (40% ellagic acid)</span><span class="amt">50mg</span><span class="dv">*</span></div>
    <div class="row"><span><b>Herbal Complex</b></span><span class="amt">100mg</span><span class="dv">*</span><span class="sub">(Consisting of indian Rhubarb, Burdock Powder, Sheep Sorrel powder and slippery Elm Powder)</span></div>
    <div class="row"><span><b>Mushroom Complex</b></span><span class="amt">80mg</span><span class="dv">*</span><span class="sub">(Consisting of Shiitake, Maitake and Reishi)</span></div>
    <div class="row"><span><b>ARA-6</b> (arabinogalactan)</span><span class="amt">20mg</span><span class="dv">*</span></div>
    <div class="row"><span><b>Olive Leaf Extract</b></span><span class="amt">50mg</span><span class="dv">*</span></div>
    <div class="foot">*Daily Values not establised.</div>
  </section>
</main>
</body>
</html>
```